Business Card Design for Software Development Company

I am looking for a business card design the incorporates my new logo (attached below).

Key information to include:
Name: Darnell Whisket
Title: CEO
Email: darnell@brovatecore.com
Phone: 418-926-7301
Website: www.brovatecore.com

NOTE: This design should be easy to edit so that we can order cards for different members of our team.

```html
<!DOCTYPE html>
<html lang="en">
<head>
<meta charset="utf-8">
<title>BrovateLabs Business Card</title>
<link href="https://fonts.googleapis.com/css2?family=Montserrat:wght@500;600;700&display=swap" rel="stylesheet">
<style>
  :root {
    --navy: #33495b;
    --ink: #2c3e50;
    --teal: #12a893;
    --orange: #e8782a;
    --red: #c93a2a;
    --paper: #ffffff;
    --backdrop: #e6e7e9;
  }
  * { margin: 0; padding: 0; box-sizing: border-box; }
  html, body {
    width: 900px; height: 1200px; overflow: hidden;
    background: var(--backdrop);
    font-family: "Montserrat", sans-serif;
  }
  .canvas { position: relative; width: 900px; height: 1200px; }

  .card {
    position: absolute; left: 135px; width: 630px; height: 360px;
    box-shadow: 0 6px 14px rgba(0,0,0,0.18);
  }
  .card-front { top: 213px; background: var(--navy); }
  .card-back { top: 627px; background: var(--paper); }

  .wordmark { position: absolute; text-align: right; }
  .wordmark-name { display: flex; align-items: center; gap: 10px; font-weight: 600; letter-spacing: -0.5px; line-height: 1; }
  .wordmark-mark { display: inline-block; }
  .wordmark-tagline { font-weight: 700; text-transform: uppercase; letter-spacing: 0.2px; margin-top: 3px; }

  .card-front .wordmark { right: 42px; top: 268px; }
  .card-front .wordmark-name { font-size: 52px; color: var(--paper); }
  .card-front .wordmark-mark { width: 30px; height: 30px; background: var(--orange); }
  .card-front .wordmark-tagline { font-size: 6px; color: var(--paper); }

  .card-back .wordmark { left: 55px; top: 160px; }
  .card-back .wordmark-name { font-size: 31px; color: var(--ink); gap: 8px; }
  .card-back .wordmark-mark { width: 18px; height: 18px; background: var(--orange); }
  .card-back .wordmark-tagline { font-size: 4.5px; color: var(--ink); }

  .divider { position: absolute; left: 315px; top: 121px; width: 2px; height: 119px; background: var(--ink); }

  .contact { position: absolute; left: 332px; top: 120px; color: var(--ink); }
  .contact-name { font-size: 24px; font-weight: 700; color: var(--teal); line-height: 1.1; }
  .contact-title { font-size: 15px; font-weight: 500; margin-top: 1px; }
  .contact-rule { width: 30px; height: 2px; margin: 3px 0 10px; background: linear-gradient(90deg, var(--teal), var(--orange)); }
  .contact-list { list-style: none; }
  .contact-item { display: flex; align-items: center; gap: 6px; font-size: 15px; font-weight: 500; height: 25px; }
  .contact-icon { width: 14px; height: 14px; flex: none; }
</style>
</head>
<body>
<main class="canvas">
  <section class="card card-front" aria-label="Card front">
    <div class="wordmark">
      <div class="wordmark-name"><span class="wordmark-mark"></span>BrovateLabs</div>
      <div class="wordmark-tagline">A division of Brovate Group</div>
    </div>
  </section>

  <section class="card card-back" aria-label="Card back">
    <div class="wordmark">
      <div class="wordmark-name"><span class="wordmark-mark"></span>BrovateLabs</div>
      <div class="wordmark-tagline">A division of Brovate Group</div>
    </div>

    <div class="divider"></div>

    <div class="contact">
      <h1 class="contact-name">Darnell Whisket</h1>
      <p class="contact-title">CEO</p>
      <div class="contact-rule"></div>
      <ul class="contact-list">
        <li class="contact-item">
          <svg class="contact-icon" viewBox="0 0 24 24" aria-hidden="true"><path fill="#d4472b" d="M6.6 10.8a15.1 15.1 0 0 0 6.6 6.6l2.2-2.2c.3-.3.7-.4 1-.2 1.1.4 2.3.6 3.6.6.6 0 1 .4 1 1V20c0 .6-.4 1-1 1A17 17 0 0 1 3 4c0-.6.4-1 1-1h3.5c.6 0 1 .4 1 1 0 1.3.2 2.5.6 3.6.1.3 0 .7-.2 1z"/></svg>
          418-926-7301
        </li>
        <li class="contact-item">
          <svg class="contact-icon" viewBox="0 0 24 24" aria-hidden="true"><rect x="2" y="5" width="20" height="14" fill="#d4472b"/><path d="M2 5l10 8 10-8" fill="none" stroke="#fff" stroke-width="1.8"/></svg>
          darnell@brovatecore.com
        </li>
        <li class="contact-item">
          <svg class="contact-icon" viewBox="0 0 24 24" aria-hidden="true"><circle cx="12" cy="12" r="10" fill="#d4472b"/><path d="M2 12h20M12 2c3 3 3 17 0 20M12 2c-3 3-3 17 0 20" fill="none" stroke="#12a893" stroke-width="1.6"/></svg>
          www.brovatecore.com
        </li>
      </ul>
    </div>
  </section>
</main>
</body>
</html>
```